Business Card

Just need business logo with phone number on it. 0487 312 556
And the following on the bottom of the card.

"Your local plumbing experts".
and emblems for kelpa card, cheque and cash

```html
<!DOCTYPE html>
<html lang="en">
<head>
<meta charset="utf-8">
<title>Harbour Line Plumbing &amp; Drainage — Business Card</title>
<link rel="stylesheet" href="https://fonts.googleapis.com/css2?family=Play:wght@400;700&display=swap">
<style>
  :root {
    --stage: #121212;
    --card-white: #ffffff;
    --brand-red: #e3232b;
    --brand-blue: #1f8fd0;
    --brand-blue-deep: #1a82c2;
    --ink: #1b1b1b;
    --rule: #9a9a9a;
    --chip-line: #bdbdbd;
  }
  * { box-sizing: border-box; margin: 0; padding: 0; }
  html, body { width: 1200px; height: 900px; overflow: hidden; background: var(--stage); }
  body { position: relative; font-family: "Play", sans-serif; }

  .card {
    position: absolute;
    top: 170px;
    width: 347px;
    height: 561px;
    box-shadow: 0 2px 6px rgba(0,0,0,0.6);
  }
  .card--front { left: 259px; background: var(--card-white); }
  .card--back { left: 631px; overflow: hidden; }

  .brand {
    position: absolute;
    top: 120px;
    left: 0;
    width: 100%;
    text-align: center;
    color: var(--brand-red);
    font-weight: 700;
    line-height: 1;
  }
  .brand__name { display: block; font-size: 30px; letter-spacing: 1.5px; }
  .brand__sub { display: block; margin-top: 8px; font-size: 11.5px; letter-spacing: 3px; }

  .contact-rule {
    position: absolute;
    top: 321px;
    left: 35px;
    width: 277px;
    height: 1px;
    background: var(--rule);
  }
  .contact-icon {
    position: absolute;
    top: 297px;
    left: 149px;
    width: 50px;
    height: 50px;
  }
  .phone-number {
    position: absolute;
    top: 355px;
    left: 0;
    width: 100%;
    text-align: center;
    font-size: 23px;
    letter-spacing: 1px;
    color: var(--ink);
  }
  .tagline {
    position: absolute;
    top: 439px;
    left: 0;
    width: 100%;
    text-align: center;
    font-size: 20.5px;
    color: var(--ink);
  }
  .payments {
    position: absolute;
    top: 488px;
    left: 63px;
    display: flex;
    gap: 13px;
    align-items: center;
  }
  .payment-kelpa {
    width: 62px;
    height: 38px;
    border: 1px solid var(--chip-line);
    background: var(--card-white);
    color: var(--ink);
    font-weight: 400;
    font-size: 15px;
    display: flex;
    align-items: center;
    justify-content: center;
  }

  .back-field {
    position: absolute;
    inset: 0;
    background: linear-gradient(160deg, var(--brand-blue) 0%, var(--brand-blue-deep) 100%);
  }
  .back-brand {
    position: absolute;
    top: 252px;
    left: 0;
    width: 100%;
    text-align: center;
    color: var(--card-white);
    font-weight: 700;
    font-size: 60px;
    letter-spacing: 14px;
    text-indent: 14px;
    line-height: 1;
  }
</style>
</head>
<body>

  <section class="card card--front" aria-label="Business card front">
    <div class="brand">
      <span class="brand__name">HARBOUR LINE</span>
      <span class="brand__sub">PLUMBING &amp; DRAINAGE PTY LTD</span>
    </div>

    <div class="contact-rule"></div>
    <svg class="contact-icon" viewBox="0 0 50 50" aria-hidden="true">
      <circle cx="25" cy="25" r="22" fill="#fff" stroke="#e3232b" stroke-width="3.5"/>
      <path d="M14 21c0-4 5-6 11-6s11 2 11 6v2h-5v-3h-12v3h-5z" fill="#1f8fd0"/>
      <path d="M18 24h14l3 10H15z" fill="#1f8fd0"/>
      <g fill="#fff">
        <rect x="21" y="26" width="2" height="2"/><rect x="24" y="26" width="2" height="2"/><rect x="27" y="26" width="2" height="2"/>
        <rect x="21" y="29" width="2" height="2"/><rect x="24" y="29" width="2" height="2"/><rect x="27" y="29" width="2" height="2"/>
      </g>
    </svg>

    <p class="phone-number">0487 312 556</p>
    <p class="tagline">Your local plumbing experts</p>

    <div class="payments">
      <div class="payment-kelpa">Kelpa</div>
      <svg width="60" height="38" viewBox="0 0 60 38" role="img" aria-label="Cash">
        <rect x="0" y="0" width="60" height="38" rx="2" fill="#000"/>
        <circle cx="30" cy="19" r="9" fill="#fff"/>
        <text x="30" y="24" text-anchor="middle" font-family="Play, sans-serif" font-weight="700" font-size="13" fill="#000">$</text>
      </svg>
      <svg width="74" height="38" viewBox="0 0 74 38" role="img" aria-label="Cheque">
        <rect x="4" y="4" width="68" height="32" fill="#fff" stroke="#000" stroke-width="1.5"/>
        <rect x="1" y="1" width="68" height="32" fill="#fff" stroke="#000" stroke-width="1.5"/>
        <line x1="8" y1="10" x2="44" y2="10" stroke="#000" stroke-width="1.2"/>
        <line x1="8" y1="16" x2="62" y2="16" stroke="#000" stroke-width="1.2"/>
        <line x1="40" y1="22" x2="62" y2="22" stroke="#000" stroke-width="1.2"/>
        <rect x="8" y="24" width="22" height="4" fill="none" stroke="#000" stroke-width="1.2"/>
      </svg>
    </div>
  </section>

  <section class="card card--back" aria-label="Business card back">
    <div class="back-field" role="img" aria-label="Blue field with faint repeated brand pattern"></div>
    <div class="back-brand">HLPD</div>
  </section>

</body>
</html>
```